RW Framewell Inc Business cards

We need business cards using our existing logo but slightly modified. Right now the logo says RW Bedrock Masonry. We want to keep the RW part of the design, but replace the Bedrock Masonry portion with "FRAMEWELL". Please see the attached file.
Ideally this would be a blank template so we can add Different Names, titles, and phone numbers later.
On the one side we want only the logo and on the other side the detail. I'm attaching an example for you to see.
Please reach out with any other questions. Our address and other details will be given out once we find a design we like.

Target Market(s)

Construction Industry

```html
<!DOCTYPE html>
<html lang="en">
<head>
<meta charset="utf-8">
<title>RW Framewell Inc Business Cards</title>
<link rel="stylesheet" href="https://fonts.googleapis.com/css2?family=Archivo+Black&family=Roboto:wght@400&display=swap">
<style>
  :root {
    --page-bg: #000000;
    --card-bg: #2b2c2f;
    --ink-light: #ffffff;
    --ink-soft: #e6e6e8;
    --divider: #4a4b4f;
    --brand-blue: #1c76c2;
  }
  * { margin: 0; padding: 0; box-sizing: border-box; }
  html, body {
    width: 1200px;
    height: 900px;
    overflow: hidden;
    background: var(--page-bg);
  }
  .canvas {
    position: relative;
    width: 1200px;
    height: 900px;
  }
  .card {
    position: absolute;
    top: 266px;
    width: 458px;
    height: 282px;
    border-radius: 14px;
    background: var(--card-bg);
  }
  .card--front { left: 138px; }
  .card--back { left: 625px; }

  .wordmark {
    position: absolute;
    font-family: "Archivo Black", sans-serif;
    font-weight: 400;
    line-height: 1;
  }
  .card--front .wordmark {
    left: 42px;
    top: 96px;
    width: 172px;
    color: var(--ink-light);
    text-align: center;
  }
  .wordmark__initials { display: block; }
  .wordmark__name { display: block; }
  .card--front .wordmark__initials { font-size: 62px; letter-spacing: 2px; }
  .card--front .wordmark__name { font-size: 19px; margin-top: 6px; letter-spacing: 0.5px; }

  .card--back .wordmark {
    left: 0;
    right: 0;
    top: 76px;
    text-align: center;
    color: var(--brand-blue);
  }
  .card--back .wordmark__initials { font-size: 88px; letter-spacing: 3px; }
  .card--back .wordmark__name { font-size: 27px; margin-top: 8px; letter-spacing: 1px; }

  .divider {
    position: absolute;
    left: 236px;
    top: 89px;
    width: 1px;
    height: 102px;
    background: var(--divider);
  }
  .details {
    position: absolute;
    left: 256px;
    top: 90px;
    color: var(--ink-soft);
    font-family: "Roboto", sans-serif;
  }
  .details__name {
    font-family: "Archivo Black", sans-serif;
    font-size: 15px;
    color: var(--ink-light);
    letter-spacing: 0.4px;
    line-height: 1.2;
  }
  .details__title {
    font-size: 13.5px;
    line-height: 1.2;
  }
  .contact-list {
    list-style: none;
    margin-top: 15px;
  }
  .contact-list li {
    display: flex;
    align-items: center;
    gap: 5px;
    font-size: 13.5px;
    line-height: 17.5px;
  }
  .contact-list svg {
    width: 13px;
    height: 13px;
    flex: none;
  }
</style>
</head>
<body>
<main class="canvas">
  <section class="card card--front" aria-label="Business card, details side">
    <div class="wordmark">
      <span class="wordmark__initials">RW</span>
      <span class="wordmark__name">FRAMEWELL</span>
    </div>
    <div class="divider"></div>
    <div class="details">
      <p class="details__name">DANIEL PORTER</p>
      <p class="details__title">Managing Director</p>
      <ul class="contact-list">
        <li>
          <svg viewBox="0 0 16 16" aria-hidden="true"><path d="M4 1.5l2.2 3-1.3 1.6c.9 2 2.4 3.5 4.4 4.4l1.6-1.3 3 2.2-1.3 2.6C7.5 14 2 8.5 1.4 2.8z" fill="none" stroke="#fff" stroke-width="1.5" stroke-linejoin="round"/></svg>
          044-555 010 234
        </li>
        <li>
          <svg viewBox="0 0 16 16" aria-hidden="true"><rect x="1" y="3" width="14" height="10" fill="none" stroke="#fff" stroke-width="1.4"/><path d="M1 3l7 6 7-6M1 13l5-5M15 13l-5-5" fill="none" stroke="#fff" stroke-width="1.4"/></svg>
          info@mailsample.com
        </li>
        <li>
          <svg viewBox="0 0 16 16" aria-hidden="true"><g fill="none" stroke="#fff" stroke-width="1.3"><circle cx="8" cy="8" r="6.8"/><ellipse cx="8" cy="8" rx="3" ry="6.8"/><path d="M1.2 8h13.6M2.3 4.5h11.4M2.3 11.5h11.4"/></g></svg>
          www.sitesample.com
        </li>
      </ul>
    </div>
  </section>

  <section class="card card--back" aria-label="Business card, logo side">
    <div class="wordmark">
      <span class="wordmark__initials">RW</span>
      <span class="wordmark__name">FRAMEWELL</span>
    </div>
  </section>
</main>
</body>
</html>
```